Homepage Real Estate Agency

I need a web design for a real estate agency in Luxembourg. A short draft for the front page can be found in the project details. (Page 1+2) The main colors of the site should be blue as shown in the project details. (Page 3)
The main target for this site is to promote real estates and a small presentation of the company.

Industry/Entity Type

Real Estate

Requirements
Must have
• On the front page estates are shown in a short preview in small boxes, on the right side is a search. The search is hidden except for the front page. The header has 4 buttons and the logo of the company.

```html
<!DOCTYPE html>
<html lang="fr">
<head>
<meta charset="utf-8">
<title>Lumen Immo – Accueil</title>
<link rel="stylesheet" href="https://fonts.googleapis.com/css2?family=Open+Sans:wght@400;600;700&family=Yanone+Kaffeesatz:wght@700&family=Arimo:wght@400&display=swap">
<style>
:root{
  --sky-top:#29aaf6;
  --sky-mid:#2188cc;
  --sky-bottom:#0c4a78;
  --nav-bg:#efefef;
  --nav-text:#555;
  --tab-white:#ffffff;
  --tab-grey:#d8d8d8;
  --panel-light:rgba(255,255,255,.12);
  --panel-dark:#0b3f68;
  --white:#ffffff;
  --card-text:#dce9f5;
  --btn-green-top:#d4f57a;
  --btn-green-bottom:#8bd632;
  --btn-yellow-top:#ffe02a;
  --btn-yellow-bottom:#f6b400;
  --field-grey:#d9d9d9;
  --footer-text:#2d8fd3;
}
*{box-sizing:border-box;margin:0;padding:0}
html,body{width:1182px;height:1200px;overflow:hidden}
body{
  position:relative;
  background:linear-gradient(180deg,var(--sky-top) 0%,var(--sky-top) 20%,var(--sky-mid) 50%,var(--sky-bottom) 100%);
  font-family:"Open Sans",sans-serif;color:var(--white);
}
.ground{position:absolute;left:0;bottom:0;width:1182px;height:90px}
.brand-tab{
  position:absolute;left:147px;top:0;width:124px;height:210px;
  background:linear-gradient(180deg,var(--tab-white) 40%,var(--tab-grey));
  border-radius:0 0 62px 62px;box-shadow:0 4px 10px rgba(0,0,0,.2);
  display:flex;flex-direction:column;align-items:center;justify-content:flex-end;padding-bottom:30px;gap:8px;
}
.brand-mark{width:44px;height:44px;border-radius:50%;background:#2f2f88}
.brand-name{font-weight:700;font-size:15px;color:#2f2f88}
.main-nav{
  position:absolute;left:332px;top:83px;width:680px;height:42px;
  background:var(--nav-bg);border-radius:3px;box-shadow:0 3px 10px rgba(0,0,0,.25);
  display:flex;align-items:center;padding-left:56px;gap:45px;
}
.main-nav a{font-size:11.5px;font-weight:700;color:var(--nav-text);text-decoration:none;letter-spacing:.2px}
.hero{position:absolute;left:332px;top:152px;width:680px;height:350px}
.hero-shadow{position:absolute;left:30px;right:30px;bottom:-22px;height:30px;background:#04121f;border-radius:0 0 50% 50%/0 0 100% 100%;filter:blur(3px);opacity:.85}
.hero-photo{position:absolute;inset:0;background:linear-gradient(180deg,#9cc2e8 0%,#3d6a2c 35%,#d8cdb0 55%,#4d7a2c 85%,#6aa03a 100%)}
.hero-dots{position:absolute;right:18px;bottom:6px;display:flex;gap:7px}
.hero-dots span{width:10px;height:10px;border-radius:50%;background:#1d3510}
.hero-dots span:first-child{background:var(--white)}
.listings{position:absolute;left:140px;top:570px;width:542px;height:540px;background:var(--panel-light);border-radius:7px}
.listing{position:absolute;width:183px}
.listing-photo{width:183px;height:124px}
.listing-title{font-size:11.5px;font-weight:700;margin:10px 0 4px 3px}
.listing-text{font-family:"Arimo",sans-serif;font-size:10px;line-height:12px;color:var(--card-text);margin-left:3px;height:44px}
.view-more{
  display:flex;align-items:center;justify-content:center;gap:5px;margin-left:95px;width:88px;height:26px;border-radius:3px;
  background:linear-gradient(180deg,var(--btn-green-top),var(--btn-green-bottom));
  color:#1c2a05;font-size:10px;font-weight:700;text-decoration:none;
}
.search{position:absolute;left:694px;top:570px;width:341px;height:537px;background:var(--panel-dark);padding:30px 0 0 23px}
.search h2{font-family:"Yanone Kaffeesatz",sans-serif;font-size:35px;letter-spacing:.5px;line-height:1;margin-bottom:16px}
.field-label{display:block;font-size:11px;font-weight:700;margin-bottom:6px}
.text-field{width:272px;height:43px;background:var(--white);border-radius:2px;margin-bottom:22px}
.select-field{position:relative;width:171px;height:43px;background:var(--white);border-radius:2px;margin-bottom:18px}
.select-field span{position:absolute;right:5px;top:5px;width:34px;height:33px;background:var(--field-grey);border-radius:2px;display:flex;align-items:center;justify-content:center}
.choice{display:flex;align-items:center;gap:14px;font-size:11px;font-weight:700;margin:0 0 13px 5px}
.choice i{width:13px;height:13px;border-radius:50%;background:var(--white);position:relative}
.choice.on i::after{content:"";position:absolute;left:4px;top:4px;width:5px;height:5px;border-radius:50%;background:var(--panel-dark)}
.search-btn{
  display:flex;align-items:center;justify-content:center;width:144px;height:43px;margin-top:10px;border-radius:2px;
  background:linear-gradient(180deg,var(--btn-yellow-top),var(--btn-yellow-bottom));
  font-family:"Yanone Kaffeesatz",sans-serif;font-size:25px;color:#1a1a1a;letter-spacing:1px;
}
.copyright{position:absolute;left:146px;top:1128px;font-family:"Arimo",sans-serif;font-size:9px;color:var(--footer-text);letter-spacing:.5px}
.footer-nav{position:absolute;left:702px;top:1128px;font-family:"Arimo",sans-serif;font-size:9px;letter-spacing:.6px;color:var(--white)}
.footer-nav a{color:var(--white);text-decoration:none}
.footer-nav b{font-weight:400;margin:0 8px}
</style>
</head>
<body>
<svg class="ground" viewBox="0 0 1182 90" aria-hidden="true"><path d="M200 90 L390 20 L1000 60 L1182 90Z" fill="#0a3d64" opacity=".5"/></svg>

<header>
  <div class="brand-tab"><span class="brand-mark"></span><span class="brand-name">Lumen Immo</span></div>
  <nav class="main-nav">
    <a href="#">A VENDRE</a><a href="#">CONSTRUCTION</a><a href="#">LOCATION</a><a href="#">CHERCHON</a>
  </nav>
</header>

<section class="hero">
  <div class="hero-shadow"></div>
  <div class="hero-photo" role="img" aria-label="Photo of a two-storey family house with garden and trees"></div>
  <div class="hero-dots"><span></span><span></span><span></span><span></span><span></span></div>
</section>

<section class="listings">
  <article class="listing" style="left:30px;top:27px">
    <div class="listing-photo" role="img" aria-label="Photo of a Mediterranean style villa" style="background:linear-gradient(180deg,#7fb0e0,#c9b58e 55%,#4f9a2e)"></div>
    <h3 class="listing-title">TITLE OF THE REAL ESTATE</h3>
    <p class="listing-text">Lorem ipsum dolor sit amet, consecte-tur adipiscing elit. Curabitur semper, odio ut dictum.</p>
    <a class="view-more" href="#">VIEW MORE <svg width="9" height="9" viewBox="0 0 9 9"><path d="M1 4.5h6M4.5 1.5l3 3-3 3" stroke="#1c2a05" stroke-width="1.4" fill="none"/></svg></a>
  </article>
  <article class="listing" style="left:324px;top:27px">
    <div class="listing-photo" role="img" aria-label="Photo of a white house with palm trees" style="background:linear-gradient(180deg,#8aa3e6,#d6d3cc 50%,#4d6b35)"></div>
    <h3 class="listing-title">TITLE OF THE REAL ESTATE</h3>
    <p class="listing-text">Lorem ipsum dolor sit amet, consecte-tur adipiscing .</p>
    <a class="view-more" href="#">VIEW MORE <svg width="9" height="9" viewBox="0 0 9 9"><path d="M1 4.5h6M4.5 1.5l3 3-3 3" stroke="#1c2a05" stroke-width="1.4" fill="none"/></svg></a>
  </article>
  <article class="listing" style="left:30px;top:279px">
    <div class="listing-photo" role="img" aria-label="Photo of a brick house with white gables" style="background:linear-gradient(180deg,#2f5fb0,#8a7a6c 55%,#4f7d34)"></div>
    <h3 class="listing-title">TITLE OF THE REAL ESTATE</h3>
    <p class="listing-text">Lorem ipsum dolor sit amet, consecte-tur adipiscing elit. Curabitur semper, odio ut dictum.</p>
    <a class="view-more" href="#">VIEW MORE <svg width="9" height="9" viewBox="0 0 9 9"><path d="M1 4.5h6M4.5 1.5l3 3-3 3" stroke="#1c2a05" stroke-width="1.4" fill="none"/></svg></a>
  </article>
  <article class="listing" style="left:324px;top:279px">
    <div class="listing-photo" role="img" aria-label="Photo of a villa with paved driveway" style="background:linear-gradient(180deg,#8fa9e8,#e0d8c4 50%,#a9a294)"></div>
    <h3 class="listing-title">TITLE OF THE REAL ESTATE</h3>
    <p class="listing-text">Lorem ipsum dolor sit amet, consecte-tur adipiscing .</p>
    <a class="view-more" href="#">VIEW MORE <svg width="9" height="9" viewBox="0 0 9 9"><path d="M1 4.5h6M4.5 1.5l3 3-3 3" stroke="#1c2a05" stroke-width="1.4" fill="none"/></svg></a>
  </article>
</section>

<aside class="search">
  <h2>FIND YOUR PERFECT HOME</h2>
  <span class="field-label">CITY</span>
  <div class="text-field"></div>
  <span class="field-label">PREFERABLE REGION</span>
  <div class="select-field"><span><svg width="12" height="7" viewBox="0 0 12 7"><path d="M0 0h12L6 7z" fill="#666"/></svg></span></div>
  <span class="field-label">BED ROOMS</span>
  <div class="select-field"><span><svg width="12" height="7" viewBox="0 0 12 7"><path d="M0 0h12L6 7z" fill="#666"/></svg></span></div>
  <span class="field-label">BUDGET RANGE</span>
  <div class="select-field" style="margin-bottom:26px"><span><svg width="12" height="7" viewBox="0 0 12 7"><path d="M0 0h12L6 7z" fill="#666"/></svg></span></div>
  <div class="choice on"><i></i>I WANT TO RENT</div>
  <div class="choice"><i></i>I WANT TO BUY</div>
  <div class="search-btn">SEARCH</div>
</aside>

<footer>
  <p class="copyright">COPYRIGHT 2012. ALL RIGHTS RESERVED.</p>
  <nav class="footer-nav"><a href="#">HOME</a><b>|</b><a href="#">A VENDRE</a><b>|</b><a href="#">CONSTRUCTION</a><b>|</b><a href="#">LOCATION</a><b>|</b><a href="#">CHERCHON</a></nav>
</footer>
</body>
</html>
```